Business Card Ayurvedic Massage

I'm starting with my ayurvedic massage business and need a business card design. The design should be inline with my brand/logo as well as with the design of my website (www.mirelo-dant.ch).
Front: logo and text "Ayurvedische Massagen"
back: name and adress (see details https://www.mirelo-dant.ch/kontakt.html)

```html
<!DOCTYPE html>
<html lang="de">
<head>
<meta charset="utf-8">
<title>Mirelo-Dant – Visitenkarte</title>
<link href="https://fonts.googleapis.com/css2?family=Open+Sans:wght@400;700&display=swap" rel="stylesheet">
<style>
  :root {
    --stage: #c9c9c9;
    --maroon: #7e1216;
    --maroon-deep: #6c0f13;
    --brown-dark: #341012;
    --gold: #d9a441;
    --gold-soft: #c9924a;
    --ink: #1d1d1d;
    --paper: #ffffff;
    --accent-red: #a3161c;
  }
  * { box-sizing: border-box; margin: 0; padding: 0; }
  html, body {
    width: 1200px; height: 1200px; overflow: hidden;
    background: var(--stage);
    font-family: "Open Sans", Arial, sans-serif;
  }
  .sheet {
    width: 1200px; height: 1200px;
    display: flex; flex-direction: column; align-items: center; justify-content: center;
    gap: 44px;
  }
  .card {
    position: relative;
    width: 860px; height: 525px;
    box-shadow: 0 10px 24px rgba(0,0,0,.22);
    overflow: hidden;
  }

  /* Front */
  .card--front { background: var(--maroon); }
  .card--front .texture {
    position: absolute; inset: 0;
    background: radial-gradient(circle at 50% 50%, var(--maroon) 0%, var(--maroon-deep) 100%);
  }
  .elephant {
    position: absolute;
    width: 190px; height: 170px;
    border-radius: 14px;
    background: linear-gradient(135deg, #e6b65a 0%, #c8862f 55%, #b5432a 100%);
    opacity: .92;
  }
  .elephant--left { left: 70px; top: 250px; }
  .elephant--right { right: 70px; top: 60px; }
  .brand {
    position: absolute; left: 290px; top: 205px; width: 330px;
    text-align: center;
  }
  .brand__name {
    font-weight: 700; font-size: 46px; color: var(--gold);
    letter-spacing: 1px;
  }
  .brand__tagline {
    margin-top: 14px;
    font-size: 25px; color: var(--gold-soft);
    letter-spacing: .5px;
  }

  /* Back */
  .card--back { background: var(--paper); }
  .contact {
    position: absolute; left: 150px; top: 90px;
    color: var(--ink);
  }
  .contact__notice { font-weight: 700; font-size: 30px; margin-bottom: 38px; }
  .contact__address { font-size: 24px; line-height: 1.35; margin-bottom: 22px; }
  .contact__list { list-style: none; font-size: 24px; line-height: 1.4; }
  .contact__list li { display: flex; align-items: center; gap: 12px; }
  .contact__list svg { width: 20px; height: 20px; flex: none; }
  .bands { position: absolute; left: 0; bottom: 0; width: 860px; height: 60px; }
</style>
</head>
<body>
<main class="sheet">

  <section class="card card--front" aria-label="Vorderseite">
    <div class="texture" role="img" aria-label="Dunkelrotes Damastmuster im Hintergrund"></div>
    <div class="elephant elephant--left" role="img" aria-label="Goldener geschmückter Elefant mit Schirm"></div>
    <div class="elephant elephant--right" role="img" aria-label="Goldener geschmückter Elefant mit Schirm"></div>
    <div class="brand">
      <div class="brand__name">Mirelo-Dant</div>
      <div class="brand__tagline">Ayurvedische Massagen</div>
    </div>
  </section>

  <section class="card card--back" aria-label="Rückseite">
    <div class="contact">
      <p class="contact__notice">Bitte Keine Werbung</p>
      <p class="contact__address">Lena Vasari, Mirelo-Dant,<br>Birkenweg 14, 8847 Talwil (SZ)</p>
      <ul class="contact__list">
        <li>
          <svg viewBox="0 0 20 20" aria-hidden="true"><path d="M5 2l3 4-2 2c1 2 3 4 5 5l2-2 4 3-2 3C9 17 3 11 2 5z" fill="var(--accent-red)"/></svg>
          +41 76 318 42 07
        </li>
        <li>
          <svg viewBox="0 0 20 20" aria-hidden="true"><rect x="2" y="5" width="16" height="11" fill="var(--accent-red)"/><path d="M2 5l8 6 8-6" fill="none" stroke="#fff" stroke-width="1.5"/></svg>
          info@mirelo-dant.ch
        </li>
        <li>
          <svg viewBox="0 0 20 20" aria-hidden="true" fill="none" stroke="var(--accent-red)" stroke-width="1.5"><circle cx="10" cy="10" r="8"/><ellipse cx="10" cy="10" rx="3.5" ry="8"/><path d="M2 10h16M3.5 6h13M3.5 14h13"/></svg>
          www.mirelo-dant.ch
        </li>
      </ul>
    </div>
    <svg class="bands" viewBox="0 0 860 60" aria-hidden="true">
      <polygon points="0,46 460,46 460,60 0,60" fill="var(--maroon)"/>
      <polygon points="470,18 860,18 860,60 478,60" fill="var(--brown-dark)"/>
    </svg>
  </section>

</main>
</body>
</html>
```